Velvet Thistle

I want my website to have a page I can easily add pictures of things for sale (beauty & clothes). An about me/company page. The main page I want to Blog on. I am a lifestyle/luxury/fashion brand. I have videos I want to link to my page from youtube/entertainment.... also too I’d like Facebook/ instagram/ Pinterest/Twitter link
I need a "Book Online" button so clients can book stylist appointment with 50% money down non refundable. Also too you can get refund insurance for personal stylist/shopper appt.
Target Market(s)
14-45 year old woman
Coding
Coded - Design and coding required
Number of Pages Required
2 page
Requirements
Must have
- Modern
- Slogan: Velvet and Thistle
- there is peaceful. there is wild. i am both at the same time. -kaj
Nice to have
- I have videos I want to link to my page..... also too I’d like Facebook/ instagram/ Twitter link
- My logo at the corner of screen or msube as a watermark for the background (just an idea)

```html
<!DOCTYPE html>
<html lang="en">
<head>
<meta charset="utf-8">
<title>Velvet Thistle — Beauty of Nature</title>
<link rel="stylesheet" href="https://fonts.googleapis.com/css2?family=Lato:wght@300;400;700&family=Playfair+Display:wght@400;700&display=swap">
<style>
:root{
  --ink:#2b2b2b;
  --muted:#8a8a8a;
  --soft:#bdbdbd;
  --line:#e4e4e4;
  --gold:#c4a062;
  --blue:#2f6fb8;
  --pink:#e6559f;
  --footer:#262626;
  --footer-line:#3a3a3a;
  --paper:#ffffff;
}
*{box-sizing:border-box;margin:0;padding:0}
html,body{width:1200px;height:2800px;overflow:hidden;background:var(--paper)}
body{font-family:'Lato',sans-serif;color:var(--ink);font-size:12px;line-height:1.6}
.canvas{position:relative;width:1200px;height:2800px;overflow:hidden}
.abs{position:absolute}
.serif{font-family:'Playfair Display',serif}

/* top bar */
.topbar{top:0;left:0;width:1200px;height:40px;display:flex;justify-content:space-between;align-items:center;padding:0 20px}
.dots{display:flex;gap:10px}
.dot{width:10px;height:10px;border-radius:50%;background:var(--ink)}
.brand{top:18px;left:0;width:1200px;text-align:center}
.brand-mark{width:34px;height:34px;border-radius:50%;background:var(--gold);margin:0 auto 8px}
.brand-name{font-family:'Playfair Display',serif;font-size:30px;letter-spacing:4px;color:var(--gold);line-height:1.1}
.nav{top:168px;left:0;width:1200px;display:flex;justify-content:center;gap:26px;font-size:10px;letter-spacing:1px;font-weight:700;border-top:1px solid var(--line);border-bottom:1px solid var(--line);padding:10px 0}

/* hero */
.hero{top:206px;left:0;width:1200px;height:330px;background:linear-gradient(180deg,#c9ccd2 0%,#9ea3ab 45%,#5c6169 80%,#3f434a 100%)}
.hero-title{right:160px;bottom:24px;color:#fff;font-size:22px;letter-spacing:2px;font-weight:700;font-family:'Lato',sans-serif}
.hero-tab{left:60px;bottom:0;width:260px;height:14px;background:var(--paper)}

/* article */
.main{left:100px;width:720px}
.post-title{top:560px;text-align:center;font-size:22px;letter-spacing:1px}
.post-date{top:596px;text-align:center;font-size:9px;color:var(--muted);letter-spacing:2px}
.copy p{font-size:11px;color:#555;margin-bottom:10px;line-height:1.65}
.figure{top:742px;height:380px;background:linear-gradient(180deg,#b9c8d6 0%,#9eb0c2 40%,#6f7f8f 70%,#d6dde3 100%)}
.caption{top:1130px;text-align:center;font-size:9px;color:var(--muted)}
.quote{font-size:15px;color:var(--soft);letter-spacing:.5px;line-height:1.6;text-transform:uppercase;margin:14px 0 16px}
.tags{top:1500px;display:flex;justify-content:space-between;align-items:center;border-bottom:1px solid var(--line);padding-bottom:10px}
.tag{display:inline-block;border:1px solid var(--line);font-size:8px;letter-spacing:1px;padding:2px 8px;margin-right:5px;color:var(--muted)}
.share{font-size:9px;color:var(--muted);letter-spacing:1px}
.rule-title{display:flex;align-items:center;gap:14px;font-size:10px;letter-spacing:2px;font-weight:700}
.rule-title::before,.rule-title::after{content:"";flex:1;height:1px;background:var(--line)}
.comment{top:1580px;display:flex;gap:22px;padding:0 20px}
.avatar{width:64px;height:64px;border-radius:50%;background:linear-gradient(135deg,#8a7b70,#3d3531);flex:none}
.comment-name{font-size:13px;font-weight:700}
.comment-text{font-size:11px;color:#555}
.related{top:1768px;display:flex;justify-content:space-between;padding:0 20px}
.card{width:210px}
.card-img{height:160px}
.card-title{font-size:9px;font-weight:700;letter-spacing:1px;margin-top:8px}
.card-date{font-size:8px;color:var(--muted)}
.reply-note{top:2090px;text-align:center;font-size:10px;color:#555}
.field{border:1px solid var(--line);background:var(--paper)}
.textarea{top:2112px;height:96px}
.inputs{top:2222px;display:flex;gap:10px}
.inputs .field{flex:1;height:26px;font-size:9px;color:var(--soft);padding:6px 8px}
.btn-post{top:2262px;left:100px;background:var(--ink);color:#fff;font-size:9px;letter-spacing:1px;padding:6px 14px}

/* sidebar */
.side{left:852px;width:250px}
.widget{border:1px solid var(--line);padding:14px}
.widget-title{font-size:9px;letter-spacing:2px;font-weight:700;text-align:center;margin-bottom:10px}
.about{top:566px}
.about-img{height:112px;background:linear-gradient(135deg,#d8d2cc,#7a6e66)}
.about p{font-size:10px;color:#555;margin-top:10px}
.sign{font-family:'Playfair Display',serif;font-style:normal;color:var(--muted);font-size:14px;text-align:right;margin-top:4px}
.subscribe{top:858px;padding:0}
.subscribe-head{background:var(--blue);color:#fff;font-size:9px;letter-spacing:2px;font-weight:700;text-align:center;padding:8px}
.subscribe-body{padding:12px 14px}
.subscribe-body .field{height:22px;margin-bottom:8px}
.btn-pink{background:var(--pink);color:#fff;font-size:8px;letter-spacing:1px;text-align:center;padding:5px;font-weight:700}
.insta{top:1032px}
.grid{display:grid;grid-template-columns:repeat(3,1fr);gap:6px}
.grid div{height:68px}
.follow{top:1384px;text-align:center}
.follow .dots{justify-content:center}
.book{top:1500px;background:var(--blue);color:#fff;text-align:center;padding:26px 16px;height:204px}
.book-title{font-size:20px;letter-spacing:1px;margin-bottom:10px}
.book-text{font-size:11px;letter-spacing:1px;line-height:1.5}
.book-text b{font-size:16px}
.book .btn-pink{width:110px;margin:16px auto 0}

/* instagram strip */
.strip-label{top:2310px;left:0;width:1200px;text-align:center;font-size:10px;letter-spacing:1px;color:var(--muted)}
.strip{top:2334px;left:0;width:1200px;height:78px;display:flex}
.strip div{flex:1}

/* footer */
.footer{top:2412px;left:0;width:1200px;height:388px;background:var(--footer);color:#cfcfcf}
.f-brand{top:50px;left:100px;text-align:center;width:160px}
.f-brand .brand-mark{width:44px;height:44px}
.f-brand .brand-name{font-size:24px}
.f-col{top:44px;width:200px}
.f-col h4{font-size:9px;letter-spacing:2px;color:#fff;font-weight:700;border-bottom:1px solid var(--footer-line);padding-bottom:8px;margin-bottom:12px}
.f-col p{font-size:10px;color:#9a9a9a;margin-bottom:8px}
.f-item{margin-bottom:14px}
.f-item b{display:block;font-size:9px;letter-spacing:1px;color:#e0e0e0}
.f-item span{font-size:8px;color:var(--muted)}
.f-input{height:22px;background:#fff;margin-bottom:8px}
.f-bottom{bottom:0;left:0;width:1200px;height:44px;border-top:1px solid var(--footer-line);display:flex;justify-content:flex-end;align-items:center;gap:20px;padding-right:100px;font-size:8px;letter-spacing:1px;color:#bbb}
</style>
</head>
<body>
<div class="canvas">

  <header>
    <div class="abs topbar">
      <div class="dots"><span class="dot"></span><span class="dot"></span><span class="dot"></span><span class="dot"></span></div>
      <div class="dots">
        <svg width="12" height="12" viewBox="0 0 12 12"><circle cx="5" cy="5" r="3.5" fill="none" stroke="#2b2b2b" stroke-width="1.5"/><line x1="7.5" y1="7.5" x2="11" y2="11" stroke="#2b2b2b" stroke-width="1.5"/></svg>
        <svg width="12" height="12" viewBox="0 0 12 12"><circle cx="9" cy="2.5" r="2" fill="#2b2b2b"/><circle cx="3" cy="6" r="2" fill="#2b2b2b"/><circle cx="9" cy="9.5" r="2" fill="#2b2b2b"/><path d="M3 6L9 2.5M3 6L9 9.5" stroke="#2b2b2b"/></svg>
      </div>
    </div>
    <div class="abs brand">
      <div class="brand-mark"></div>
      <div class="brand-name">VELVET<br>THISTLE</div>
    </div>
    <nav class="abs nav">
      <span>HOME</span><span>SERVICES</span><span>BLOG</span><span>SHOP</span><span>ABOUT ME</span><span>CONTACT</span><span>BOOK AN APPOINTMENT</span>
    </nav>
  </header>

  <section class="abs hero" role="img" aria-label="City skyline at dusk with a suspension bridge over the river">
    <div class="abs hero-tab"></div>
    <div class="abs hero-title">BIG CITY LIGHTS</div>
  </section>

  <article>
    <h1 class="abs main post-title serif">BEAUTY OF NATURE</h1>
    <div class="abs main post-date">JUNE 12, 2018</div>
    <div class="abs main copy" style="top:624px">
      <p>Soft mornings begin with light linen, a warm cup and a slow walk through the garden. We gathered the pieces that made this season feel calm, from gentle knits to quiet tones of sand, cream and sage that rest easy on the skin and the mind alike.</p>
      <p>Every look here was styled outdoors, letting the trees and open sky set the mood. Keep the shapes loose, the fabrics natural and the jewelry simple, then let one bold detail carry the rest of the outfit through the whole day.</p>
    </div>
    <div class="abs main figure" role="img" aria-label="City waterfront skyline under a pale blue sky"></div>
    <div class="abs main caption">Morning by the river</div>
    <div class="abs main copy" style="top:1160px">
      <p>Nature reminds us to slow down. A long weekend away gave us space to test new textures, mix vintage finds with fresh pieces and rethink what feels truly effortless for everyday wear.</p>
      <div class="quote">There is peaceful. There is wild. I am both at the same time. — Kaj</div>
      <p>Take the colours you love outside and see how they change in daylight. The best wardrobe is one that moves with you, from quiet mornings to bright evenings out in the city.</p>
      <p>Share your own favourite outdoor looks with us below, and tell us which pieces you reach for first when the weather turns warm again.</p>
    </div>

    <div class="abs main tags">
      <div><span class="tag">BEAUTY</span><span class="tag">FASHION</span><span class="tag">TRAVEL</span></div>
      <div class="share">SHARE</div>
    </div>

    <div class="abs main rule-title" style="top:1542px">ONE COMMENT</div>
    <div class="abs main comment">
      <div class="avatar" role="img" aria-label="Commenter portrait"></div>
      <div>
        <div class="comment-name serif">Mara Oakes</div>
        <div class="comment-text">Such a calm and lovely set of looks. I adore the linen pieces and the soft colours. Saving this for my next trip away.</div>
      </div>
    </div>

    <div class="abs main rule-title" style="top:1724px">YOU MIGHT ALSO LIKE</div>
    <div class="abs main related">
      <div class="card"><div class="card-img" role="img" aria-label="Portrait of a woman with dark hair" style="background:linear-gradient(135deg,#a89a92,#3c3532)"></div><div class="card-title">FASHION MODEL SHOOT</div><div class="card-date">MAY 20, 2018</div></div>
      <div class="card"><div class="card-img" role="img" aria-label="Snowy winter forest" style="background:linear-gradient(180deg,#c7d3de,#eef1f4 60%,#8b8f93)"></div><div class="card-title">COLD WINTER DAYS</div><div class="card-date">MAY 8, 2018</div></div>
      <div class="card"><div class="card-img" role="img" aria-label="Bare trees on a snowy hillside" style="background:linear-gradient(180deg,#d9dcdf,#b9bcbf 55%,#f2f2f2)"></div><div class="card-title">FOREST TRAVELS</div><div class="card-date">APRIL 30, 2018</div></div>
    </div>

    <div class="abs main rule-title" style="top:2046px">LEAVE A REPLY</div>
    <div class="abs main reply-note">Your email address will not be published. Required fields are marked *</div>
    <div class="abs main field textarea"></div>
    <div class="abs main inputs"><div class="field">Name*</div><div class="field">Email*</div><div class="field">Website</div></div>
    <div class="abs btn-post">POST COMMENT</div>
  </article>

  <aside>
    <div class="abs side widget about">
      <div class="widget-title">ABOUT ME</div>
      <div class="about-img" role="img" aria-label="Portrait of the stylist"></div>
      <p>Stylist and shopper sharing easy luxury, beauty finds and outfits for every day.</p>
      <div class="sign">Noor</div>
    </div>
    <div class="abs side widget subscribe">
      <div class="subscribe-head">SUBSCRIBE TO NEWSLETTER</div>
      <div class="subscribe-body"><div class="field"></div><div class="btn-pink">SUBSCRIBE</div></div>
    </div>
    <div class="abs side widget insta">
      <div class="widget-title">INSTAGRAM</div>
      <div class="grid" role="img" aria-label="Grid of fashion and lifestyle photos">
        <div style="background:#8d7a6e"></div><div style="background:#c9c3bc"></div><div style="background:#5a4e48"></div>
        <div style="background:#d8d0c8"></div><div style="background:#3f3936"></div><div style="background:#a99a90"></div>
        <div style="background:#6c625c"></div><div style="background:#bdb3aa"></div><div style="background:#4a4340"></div>
      </div>
    </div>
    <div class="abs side widget follow">
      <div class="widget-title">FOLLOW US ON</div>
      <div class="dots"><span class="dot"></span><span class="dot"></span><span class="dot"></span><span class="dot"></span></div>
    </div>
    <div class="abs side book">
      <div class="book-title">BOOK ONLINE</div>
      <div class="book-text">BOOK STYLIST APPOINTMENT<br>WITH <b>50%</b> DISCOUNT</div>
      <div class="btn-pink">BOOK NOW</div>
    </div>
  </aside>

  <div class="abs strip-label">@velvetthistle</div>
  <div class="abs strip" role="img" aria-label="Row of street style and accessory photos">
    <div style="background:#b8b2ac"></div><div style="background:#4d4642"></div><div style="background:#8f8680"></div><div style="background:#2f2b29"></div><div style="background:#a39a94"></div><div style="background:#d4d0cc"></div><div style="background:#6b5f56"></div><div style="background:#3a3431"></div><div style="background:#9c8f85"></div>
  </div>

  <footer class="abs footer">
    <div class="abs f-brand"><div class="brand-mark"></div><div class="brand-name">VELVET<br>THISTLE</div></div>
    <div class="abs f-col" style="left:380px">
      <h4>NEWSLETTER</h4>
      <p>Get new posts and offers first.</p>
      <div class="f-input"></div>
      <div class="btn-pink">SUBSCRIBE</div>
    </div>
    <div class="abs f-col" style="left:620px">
      <h4>RECENT POSTS</h4>
      <div class="f-item"><b>BEAUTY OF NATURE</b><span>JUNE 12, 2018</span></div>
      <div class="f-item"><b>FASHION MODEL SHOOT</b><span>MAY 20, 2018</span></div>
      <div class="f-item"><b>COLD WINTER DAYS</b><span>MAY 8, 2018</span></div>
    </div>
    <div class="abs f-col" style="left:880px">
      <h4>POPULAR POSTS</h4>
      <div class="f-item"><b>CITY NIGHT LOOKS</b><span>APRIL 22, 2018</span></div>
      <div class="f-item"><b>SPRING DRESS EDIT</b><span>APRIL 10, 2018</span></div>
      <div class="f-item"><b>FOREST TRAVELS</b><span>APRIL 30, 2018</span></div>
    </div>
    <div class="abs f-bottom"><span>HOME</span><span>SHOP</span><span>ABOUT</span><span>CONTACT</span></div>
  </footer>

</div>
</body>
</html>
```